Anesthesia Medical Practice Business Card

We need a business card to hand out to surgeons with my basic information. Something that stands out but is not over the top. The medical community is rather conservative. I'd like them to call me first when flipping through their rolodex of anesthesiologists. I'd like the card to communicate confidence, control, professionalism yet serenity. I don't want the card to be pricey to print.

he logo will be provided as a vector graphic in addition to a complete business card design including the logo

Ravi Pell Okonedo, M.D.
Board Certified Anesthesiologist

(310) 555-0186

rokonedo@mailvane.net

Mailing Address:
48315 Corbel Ave.
Suite 270-4863
Los Angeles, CA 90024

A logo that inegrates my initials perhaps
RO MD
My initials are RO and MD as in Medical Doctor

or
perhaps a physician in surgical mask and cap caring for a patient

Target Market(s)

Surgeons who need anesthesia services

Industry/Entity Type

Medical

Requirements
Must have
• the logo will be provided as a vector graphic in addition to a complete business card design including the logo

Ravi Pell Okonedo, M.D.

(310) 555-0186

rokonedo@mailvane.net

Mailing Address:
48315 Corbel Ave.
Suite 270-4863
Los Angeles, CA 90024

Nice to have
• A logo that inegrates my initials perhaps
RO MD

or

```html
<!DOCTYPE html>
<html lang="en">
<head>
<meta charset="utf-8">
<title>Ravi Pell Okonedo, M.D. — Business Card</title>
<link href="https://fonts.googleapis.com/css2?family=Quicksand:wght@500;600;700&display=swap" rel="stylesheet">
<style>
  :root {
    --page-bg: #3a322d;
    --card-black: #0c0c0d;
    --card-sheen: #2a2b2d;
    --ink-white: #f2f2f2;
    --ink-soft: #c9c9c9;
    --divider: rgba(255,255,255,0.16);
  }
  * { margin: 0; padding: 0; box-sizing: border-box; }
  html, body {
    width: 1200px; height: 1000px; overflow: hidden;
    background: var(--page-bg);
    font-family: "Quicksand", sans-serif;
  }
  .stage {
    width: 1200px; height: 1000px;
    display: flex; align-items: center; justify-content: center;
  }
  .business-card {
    position: relative;
    width: 840px; height: 480px;
    background:
      linear-gradient(115deg, transparent 35%, rgba(255,255,255,0.06) 48%, transparent 62%),
      radial-gradient(ellipse at 55% 25%, var(--card-sheen) 0%, var(--card-black) 70%);
    box-shadow: 0 20px 40px rgba(0,0,0,0.45);
    color: var(--ink-white);
  }
  .monogram {
    position: absolute; left: 110px; top: 150px;
    width: 260px; text-align: center;
    font-size: 84px; font-weight: 600; letter-spacing: 2px;
    color: var(--ink-white);
  }
  .divider {
    position: absolute; left: 430px; top: 60px;
    width: 1px; height: 250px;
    background: linear-gradient(to bottom, transparent, var(--divider), transparent);
  }
  .identity { position: absolute; left: 470px; top: 150px; }
  .identity .name { font-size: 24px; font-weight: 600; letter-spacing: 1px; }
  .identity .title { font-size: 15px; font-weight: 500; color: var(--ink-soft); letter-spacing: 0.6px; margin-top: 2px; }
  .contact { margin-top: 18px; list-style: none; }
  .contact li {
    display: flex; align-items: center; gap: 10px;
    font-size: 16px; font-weight: 500; letter-spacing: 0.6px; line-height: 26px;
  }
  .contact svg { width: 16px; height: 14px; flex: none; }
  .mailing {
    position: absolute; left: 560px; top: 330px;
    font-size: 16px; font-weight: 500; letter-spacing: 0.6px; line-height: 24px;
  }
  .mailing .label { font-weight: 700; }
</style>
</head>
<body>
<main class="stage">
  <article class="business-card">
    <div class="monogram">RO MD</div>
    <div class="divider"></div>

    <section class="identity">
      <h1 class="name">Ravi Pell Okonedo, M.D.</h1>
      <p class="title">Board Certified Anesthesiologist</p>
      <ul class="contact">
        <li>
          <svg viewBox="0 0 16 14" aria-hidden="true">
            <path d="M1 5 Q8 0 15 5 L13 7 L11 5 L5 5 L3 7 Z" fill="var(--ink-white)"/>
            <rect x="3" y="7" width="10" height="6" rx="1" fill="var(--ink-white)"/>
          </svg>
          <span>(310) 555-0186</span>
        </li>
        <li>
          <svg viewBox="0 0 16 14" aria-hidden="true">
            <rect x="1" y="2" width="14" height="10" fill="none" stroke="var(--ink-white)" stroke-width="1.5"/>
            <path d="M1 2 L8 8 L15 2" fill="none" stroke="var(--ink-white)" stroke-width="1.5"/>
          </svg>
          <span>rokonedo@mailvane.net</span>
        </li>
      </ul>
    </section>

    <address class="mailing">
      <div class="label">Mailing Address:</div>
      <div>48315 Corbel Ave.</div>
      <div>Suite 270-4863</div>
      <div>Los Angeles, CA 90024</div>
    </address>
  </article>
</main>
</body>
</html>
```